HomebrewCampusScores blogger needs quillet book cover

The title for the book is "Building School Shortlists: Your Handbook for Reading Campus Pages to Spend Less on Smarter Learning"

Title must legible for Quillet store. I only need to front, no back or spine. The cover should be optimized to display on Veranto. Image size should be 1880x2500.

This book isn’t about how to apply to college or which classes to take or how to score higher on the QRT. It’s only focus is on how to use college websites to create a better college list. This is part of my general approach for families to use information important to their situation to find affordable colleges. I've attached a file with some covers from the category I like. I'm pretty flexible regarding colors, fonts, etc.

Target Market(s)

Parents of high school students worried about paying for college.

Industry/Entity Type

College

Requirements
Must have
• Title must be legible at small size.

```html
<!DOCTYPE html>
<html lang="en">
<head>
<meta charset="utf-8">
<title>Building School Shortlists — Book Cover</title>
<link rel="stylesheet" href="https://fonts.googleapis.com/css2?family=Roboto+Mono:wght@500;600&family=EB+Garamond:wght@500&display=swap">
<style>
  :root {
    --sky: #cfe0f7;
    --lavender: #e4dcf5;
    --mist: #f7f8fc;
    --peach: #f7ead2;
    --grid-line: rgba(255,255,255,0.95);
    --paper: #fbfbfc;
    --paper-edge: #eef0f4;
    --ink: #4a4a4a;
    --subtitle: #7ea6e2;
    --tape: #c9dcec;
    --pig-pink: #f2b3d8;
    --pig-light: #f7c9e3;
  }
  * { margin: 0; padding: 0; box-sizing: border-box; }
  html, body { width: 864px; height: 1200px; overflow: hidden; }
  body { background: var(--mist); }

  .cover {
    position: relative;
    width: 864px;
    height: 1200px;
    overflow: hidden;
    background:
      radial-gradient(ellipse 60% 35% at 90% 95%, var(--peach), transparent 70%),
      radial-gradient(ellipse 55% 40% at 8% 8%, var(--sky), transparent 70%),
      radial-gradient(ellipse 60% 40% at 95% 10%, var(--lavender), transparent 70%),
      radial-gradient(ellipse 50% 30% at 15% 85%, var(--sky), transparent 70%),
      var(--mist);
  }
  .grid {
    position: absolute; inset: 0;
    background-image:
      repeating-linear-gradient(to right, var(--grid-line) 0 3px, transparent 3px 58px),
      repeating-linear-gradient(to bottom, var(--grid-line) 0 3px, transparent 3px 58px);
    background-position: 8px 0, 0 12px;
  }

  .tape-art { position: absolute; background: var(--tape); opacity: 0.6; }
  .tape-art--left { left: 0; top: 20px; width: 240px; height: 150px; }
  .tape-art--right { right: 0; top: 30px; width: 210px; height: 180px; }

  .notepaper-art {
    position: absolute;
    left: 73px; top: 96px;
    width: 708px; height: 516px;
    background: linear-gradient(180deg, var(--paper), var(--paper-edge));
  }

  .title {
    position: absolute;
    left: 170px;
    width: 600px;
    display: block;
    text-align: center;
    font-family: "Roboto Mono", monospace;
    font-weight: 600;
    color: var(--ink);
    line-height: 1;
    transform-origin: center top;
    text-shadow: 1px 2px 2px rgba(0,0,0,0.18);
  }
  .title--top { top: 176px; font-size: 96px; letter-spacing: 14px; padding-left: 14px; transform: scaleY(1.15); }
  .title--main { top: 282px; font-size: 134px; letter-spacing: 0; transform: scaleY(1.25); }
  .title--bottom { top: 458px; font-size: 64px; letter-spacing: 16px; padding-left: 16px; transform: scaleY(1.3); }

  .piggy-art {
    position: absolute;
    left: 276px; top: 622px;
    width: 312px; height: 338px;
    border-radius: 24px;
    background: linear-gradient(180deg, var(--pig-light), var(--pig-pink));
  }

  .subtitle {
    position: absolute;
    left: 0; right: 0; top: 990px;
    text-align: center;
    font-family: "EB Garamond", serif;
    font-weight: 500;
    font-size: 42px;
    line-height: 58px;
    color: var(--subtitle);
    text-shadow: 1px 1px 1px rgba(80,110,170,0.25);
  }

  .author {
    position: absolute;
    left: 0; right: 0; top: 1124px;
    text-align: center;
    font-family: "Roboto Mono", monospace;
    font-weight: 500;
    font-size: 44px;
    letter-spacing: 9px;
    padding-left: 9px;
    color: var(--ink);
  }
</style>
</head>
<body>
<main class="cover">
  <div class="grid"></div>

  <div class="tape-art tape-art--left" role="img" aria-label="Strip of translucent tape holding the top left corner of the note paper"></div>
  <div class="tape-art tape-art--right" role="img" aria-label="Strip of translucent tape holding the top right corner of the note paper"></div>

  <div class="notepaper-art" role="img" aria-label="Torn sheet of ruled spiral notebook paper behind the title"></div>

  <h1>
    <span class="title title--top">BUILDING</span>
    <span class="title title--main">SCHOOL</span>
    <span class="title title--bottom">SHORTLISTS</span>
  </h1>

  <div class="piggy-art" role="img" aria-label="Pink piggy bank wearing a black graduation cap, a gold dollar coin dropping into its slot and a mouse pointer clicking on it"></div>

  <p class="subtitle">Your Handbook for Reading Campus Pages<br>to Spend Less on Smarter Learning</p>

  <p class="author">MARLENE KOWALCZYK</p>
</main>
</body>
</html>
```